Flyer-Design für Designer-Schmuck
Großartig - sehr gut !! Super zu frieden !!
Zielgruppe
Wir produzieren außergewöhnlichen und hochwertigen Designer-Schmuck aus Lüster-Bleikristallen für eine modebewusstes Publikum. Der Flyer wird als Beipack-Flyer unseren Versendungen beigefügt und enthält Informationen, sowie Hinweise für unsere Kunden über Funkelwerk, zu Nachhaltigkeit und Pflege.
Aufgabenstellung
nicht größer als DIN A5 | mindestens 2 oder mehr Seiten | Sollte die Aufteilung der Texte 6 Seiten erfordern sind auch 6 Seiten in Ordnung | Design und Layout sind sonst wenig Grenzen gesetzt - wir lassen uns gerne von Euren Vorschlägen begeistern, gerne aber mit Wiedererkennungswert zur Webseite https://funkelwerk-hamburg.de

```html
<!DOCTYPE html>
<html lang="de">
<head>
<meta charset="utf-8">
<title>Funkelwerk Hamburg – Flyer</title>
<link href="https://fonts.googleapis.com/css2?family=Montserrat:wght@400;500;600;700&display=swap" rel="stylesheet">
<style>
  :root{
    --purple:#7b2a83;
    --purple-soft:#9a5aa0;
    --panel-grey:#d8d7db;
    --paper:#ffffff;
    --text:#4a4a4a;
    --rule:#b48cb8;
    --bg:#ffffff;
  }
  *{box-sizing:border-box;margin:0;padding:0}
  html,body{width:1200px;height:2646px;overflow:hidden;background:var(--bg)}
  body{font-family:"Montserrat",sans-serif;color:var(--text);position:relative}
  .fold-guide{position:absolute;left:600px;top:500px;width:1px;height:1646px;background:#555}
  .spread{position:absolute;left:96px;width:720px;height:512px;transform:scale(1.4);transform-origin:0 0;display:flex;box-shadow:0 3px 6px rgba(0,0,0,.18)}
  .spread--outside{top:566px}
  .spread--inside{top:1363px}
  .panel{position:relative;width:360px;height:512px;overflow:hidden}
  .panel--grey{background:var(--panel-grey)}
  .panel--white{background:var(--paper)}
  .abs{position:absolute}
  .purple{color:var(--purple)}
  .photo{position:absolute}

  /* back cover */
  .intro-title{left:59px;top:369px;font-size:9px;font-weight:600;color:var(--purple)}
  .intro-text{left:59px;top:383px;width:250px;font-size:6px;line-height:8.6px}
  .intro-text p+p{margin-top:6px}
  .rule{position:absolute;height:1px;background:var(--rule)}
  .contacts{left:59px;top:445px;display:flex;gap:16px;font-size:4px;line-height:5.4px}
  .contact{display:flex;gap:3px}
  .contact b{font-weight:700}
  .contact svg{width:5px;height:5px;flex:none;margin-top:.5px}
  .web{left:0;width:359px;text-align:center;top:470px;font-size:9px;font-weight:600;color:var(--purple)}

  /* front cover */
  .brand{left:0;width:360px;text-align:center;top:25px;color:var(--purple)}
  .brand-name{font-size:25px;font-weight:700;line-height:28px;letter-spacing:.2px}
  .brand-city{font-size:9px;letter-spacing:.6px;line-height:10px}
  .tagline{left:0;width:360px;text-align:center;top:445px;color:var(--purple)}
  .tagline h1{font-size:13px;font-weight:600;line-height:16px}
  .tagline p{font-size:9.5px;letter-spacing:.4px;margin-top:3px}

  /* inside left */
  .head-band{position:absolute;left:0;top:0;width:360px;height:90px;background:var(--panel-grey)}
  .section-title{position:absolute;left:0;width:360px;text-align:center;color:var(--purple)}
  .section-title h2{font-size:12.5px;font-weight:600;line-height:15px}
  .section-title p{font-size:9.5px;line-height:12px;margin-top:2px;letter-spacing:.3px}
  .body-copy{left:21px;top:106px;width:318px;font-size:6.1px;line-height:9px}
  .body-copy p+p{margin-top:6px}
  .features{position:absolute;left:188px;top:333px}
  .feature{display:flex;gap:8px;height:39px}
  .tick{width:18px;height:18px;flex:none}
  .feature-name{font-size:8.6px;line-height:10px;color:#555}
  .feature-note{font-size:5.2px;line-height:6.4px;color:#555}

  /* inside right */
  .lead{left:19px;top:58px;width:325px;font-size:6px;line-height:8.5px}
  .pledges{position:absolute;left:19px;top:92px;display:grid;grid-template-columns:166px 160px;row-gap:14px}
  .pledge{display:flex;gap:6px}
  .pledge .tick{width:17px;height:17px}
  .notice{position:absolute;left:19px;width:321px;height:13px;border:1px solid var(--purple-soft);color:var(--purple);font-size:5.6px;text-align:center;line-height:11px}
  .care{position:absolute;left:19px;top:267px;display:grid;grid-template-columns:168px 150px}
  .care .ring{width:18px;height:18px;flex:none}
  .warnings{left:19px;top:353px;width:322px;font-size:4.4px;line-height:5.8px}
  .warnings p+p{margin-top:5px}
  .warnings b{font-weight:700}
</style>
</head>
<body>

<div class="fold-guide"></div>

<!-- outside: back cover + front cover -->
<section class="spread spread--outside">
  <div class="panel panel--grey back-cover">
    <h3 class="abs intro-title">Lerne uns kennen</h3>
    <div class="abs intro-text">
      <p>Auf unserer Website findest du unser gesamtes Sortiment – zum Beispiel edle Halsketten, elegante Ohrringe und verspielte Armbänder.</p>
      <p>Wir freuen uns auf deinen Besuch!</p>
    </div>
    <div class="rule" style="left:59px;top:432px;width:240px"></div>
    <div class="abs contacts">
      <div class="contact">
        <svg viewBox="0 0 10 10"><path d="M5 9.5C2.5 6.5 1.5 5 1.5 3.5a3.5 3.5 0 0 1 7 0C8.5 5 7.5 6.5 5 9.5z" fill="var(--purple)"/><circle cx="5" cy="3.6" r="1.3" fill="#fff"/></svg>
        <div><b>Funkelwerk Hamburg (Einzelunternehmung)</b><br>Lindenweg 12 | 21000 Musterdorf</div>
      </div>
      <div class="contact">
        <svg viewBox="0 0 10 10"><path d="M2 1l2 .3.7 2.2-1.2 1a6 6 0 0 0 2.5 2.5l1-1.2 2.2.7L9 8.5C9 9 8.5 9.5 8 9.5 4.3 9.2.8 5.7.5 2 .5 1.5 1 1 2 1z" fill="var(--purple)"/></svg>
        <div><b>Telefon:</b><br>+49 (0)151 - 00 00 00 00</div>
      </div>
      <div class="contact">
        <svg viewBox="0 0 10 10"><rect x=".5" y="2" width="9" height="6.5" rx=".8" fill="var(--purple)"/><path d="M1 2.5l4 3 4-3" stroke="#fff" stroke-width=".8" fill="none"/></svg>
        <div><b>E-Mail:</b><br>info@funkelwerk-hamburg.de</div>
      </div>
    </div>
    <div class="abs web">www.funkelwerk-hamburg.de</div>
  </div>

  <div class="panel panel--grey front-cover">
    <div class="abs brand">
      <div class="brand-name">Funkelwerk</div>
      <div class="brand-city">HAMBURG</div>
    </div>
    <div class="photo" role="img" aria-label="Silberner Ohrring mit violettem Kristalltropfen" style="left:300px;top:0;width:24px;height:82px;background:linear-gradient(180deg,#e6e6ea,#c9c5d0 60%,#7a5fb0)"></div>
    <div class="photo" role="img" aria-label="Werkbank mit Schalen voller Kristalle und Werkzeug" style="left:0;top:104px;width:152px;height:100px;background:linear-gradient(160deg,#a48a74,#d9d4d0 55%,#8c7460)"></div>
    <div class="photo" role="img" aria-label="Orangefarbene Lüsterkristalle in Nahaufnahme" style="left:0;top:209px;width:152px;height:100px;background:linear-gradient(150deg,#d8d2cc,#d99a6c 50%,#b9a99a)"></div>
    <div class="photo" role="img" aria-label="Klare Kristallbehänge eines Kronleuchters" style="left:0;top:314px;width:152px;height:101px;background:linear-gradient(170deg,#6d6a68,#c6c4c2 50%,#8a8684)"></div>
    <div class="photo" role="img" aria-label="Atelierraum mit Kronleuchtern, Spiegel und Büste" style="left:158px;top:104px;width:154px;height:151px;background:linear-gradient(170deg,#9c8f86,#e3e0dc 55%,#7f6f66)"></div>
    <div class="photo" role="img" aria-label="Helle Werkstatt mit Regalen, Arbeitstisch und Fenster" style="left:158px;top:262px;width:154px;height:153px;background:linear-gradient(175deg,#d9d6d3,#f0eeec 50%,#8a4a58)"></div>
    <div class="abs tagline">
      <h1>Liebevoll gefertigte Schmuckstücke</h1>
      <p>SO EINZIGARTIG WIE DU</p>
    </div>
  </div>
</section>

<!-- inside -->
<section class="spread spread--inside">
  <div class="panel panel--white about">
    <div class="head-band"></div>
    <div class="section-title" style="top:30px">
      <h2>Einzigartige, luxuriöse Schmuckstücke</h2>
      <p>FÜR DICH!</p>
    </div>
    <div class="abs body-copy">
      <p>Mit den Schmuckstücken von Funkelwerk Hamburg bewahrst du einen Teil einer magisch anmutenden Vergangenheit und bringst zugleich Eleganz und Luxus in deinen Alltag.</p>
      <p>Sicher kennst du die großen, glitzernden Kronleuchter, die in prunkvollen Schlössern hängen und ihre Umgebung mit Schönheit, Glanz und Freude füllen. Seit Generationen begleiten und faszinieren sie uns, tragen Geheimnisse und Geschichten in sich und haben besondere Momente miterlebt.</p>
      <p>Diesen Glanz und diese Erinnerung an die Geschichten alter Zeiten fangen wir in den individuell gefertigten Miniatur-Lüstern ein, welche die meisten der Funkelwerk-Schmuckstücke zieren. Zusätzlich wählen wir mit großer Sorgfalt einzelne Kristalle aus und verarbeiten beide Elemente zu edlen, wahrlich einzigartigen Schmuckstücken.</p>
      <p>Ob kraftvoll in intensiven Farben oder zeitlos und dezent: Mit Funkelwerk wird dein Leben ein bisschen mystischer, luxuriöser oder einfach schöner – unsere Art, unsere Liebe zum Lüster mit dir zu teilen.</p>
    </div>
    <div class="rule" style="left:21px;top:310px;width:319px;background:var(--purple-soft)"></div>
    <div class="photo" role="img" aria-label="Porträt einer Frau mit rotem Kristallohrring" style="left:21px;top:330px;width:148px;height:182px;background:linear-gradient(160deg,#d9cfc6,#e8ddd3 45%,#b49582)"></div>
    <div class="features">
      <div class="feature"><svg class="tick" viewBox="0 0 20 20"><circle cx="10" cy="10" r="10" fill="var(--purple)"/><path d="M5.5 10.2l3 3 6-6.2" stroke="#fff" stroke-width="2" fill="none" stroke-linecap="round"/></svg><div><div class="feature-name">einzigartig</div><div class="feature-note">sind unverwechselbare Einzelstücke</div></div></div>
      <div class="feature"><svg class="tick" viewBox="0 0 20 20"><circle cx="10" cy="10" r="10" fill="var(--purple)"/><path d="M5.5 10.2l3 3 6-6.2" stroke="#fff" stroke-width="2" fill="none" stroke-linecap="round"/></svg><div><div class="feature-name">nachhaltig</div><div class="feature-note">werden unter hohen Anforderungen<br>an Nachhaltigkeit produziert</div></div></div>
      <div class="feature"><svg class="tick" viewBox="0 0 20 20"><circle cx="10" cy="10" r="10" fill="var(--purple)"/><path d="M5.5 10.2l3 3 6-6.2" stroke="#fff" stroke-width="2" fill="none" stroke-linecap="round"/></svg><div><div class="feature-name">handgemacht</div><div class="feature-note">werden von Hand gearbeitet</div></div></div>
      <div class="feature"><svg class="tick" viewBox="0 0 20 20"><circle cx="10" cy="10" r="10" fill="var(--purple)"/><path d="M5.5 10.2l3 3 6-6.2" stroke="#fff" stroke-width="2" fill="none" stroke-linecap="round"/></svg><div><div class="feature-name">qualität</div><div class="feature-note">aus echten Kristallen und<br>925er Sterlingsilber</div></div></div>
    </div>
  </div>

  <div class="panel panel--white sustainability">
    <div class="section-title" style="top:15px">
      <h2>unser Nachhaltigkeitsversprechen</h2>
      <p>NACHHALTIGKEIT IST UNS WICHTIG</p>
    </div>
    <p class="abs lead">Es ist uns wichtig, unseren Beitrag zu den hohen Klimazielen unseres Landes zu leisten. Deshalb setzen wir folgende Maßnahmen für mehr Nachhaltigkeit um:</p>
    <div class="pledges">
      <div class="pledge"><svg class="tick" viewBox="0 0 20 20"><circle cx="10" cy="10" r="10" fill="var(--purple)"/><path d="M5.5 10.2l3 3 6-6.2" stroke="#fff" stroke-width="2" fill="none" stroke-linecap="round"/></svg><div><div class="feature-name">recycling</div><div class="feature-note">wir verwenden zum großen Teil<br>wiederverwendete Kristalle</div></div></div>
      <div class="pledge"><svg class="tick" viewBox="0 0 20 20"><circle cx="10" cy="10" r="10" fill="var(--purple)"/><path d="M5.5 10.2l3 3 6-6.2" stroke="#fff" stroke-width="2" fill="none" stroke-linecap="round"/></svg><div><div class="feature-name">regional</div><div class="feature-note">unsere Fassung (in Form eines Lüsters)<br>wird regional gefertigt</div></div></div>
      <div class="pledge"><svg class="tick" viewBox="0 0 20 20"><circle cx="10" cy="10" r="10" fill="var(--purple)"/><path d="M5.5 10.2l3 3 6-6.2" stroke="#fff" stroke-width="2" fill="none" stroke-linecap="round"/></svg><div><div class="feature-name">rücknahme</div><div class="feature-note">sende die Acrylplatten zurück und<br>wir verwenden sie für unsere Mus-<br>ter und Ausstellungsstücke</div></div></div>
      <div class="pledge"><svg class="tick" viewBox="0 0 20 20"><circle cx="10" cy="10" r="10" fill="var(--purple)"/><path d="M5.5 10.2l3 3 6-6.2" stroke="#fff" stroke-width="2" fill="none" stroke-linecap="round"/></svg><div><div class="feature-name">nachhaltig</div><div class="feature-note">werden unter hohen Anforderungen<br>an Nachhaltigkeit produziert</div></div></div>
    </div>
    <div class="notice" style="top:188px">Die Gravuren führen wir selbst durch und dadurch entfallen unnötige Transportwege.</div>
    <div class="rule" style="left:19px;top:221px;width:321px;background:var(--purple-soft)"></div>
    <div class="section-title" style="top:237px"><h2>Pflegetipps &amp; Sicherheitshinweise</h2></div>
    <div class="care">
      <div class="pledge"><svg class="ring" viewBox="0 0 20 20"><circle cx="10" cy="10" r="9" fill="none" stroke="var(--purple)" stroke-width="1.4"/><rect x="6" y="7" width="8" height="6" rx="1" fill="none" stroke="var(--purple)" stroke-width="1.2"/></svg><div><div class="feature-name">Funkelwerkglas</div><div class="feature-note">schützt vor äußeren Einflüssen und<br>erhält die Schönheit und den Glanz<br>deiner Schmuckstücke</div></div></div>
      <div class="pledge"><svg class="ring" viewBox="0 0 20 20"><circle cx="10" cy="10" r="9" fill="none" stroke="var(--purple)" stroke-width="1.4"/><path d="M10 5.5l4 4.5-4 4.5-4-4.5z" fill="none" stroke="var(--purple)" stroke-width="1.2"/></svg><div><div class="feature-name">Pflegehinweis</div><div class="feature-note">verwende ein Silberputztuch oder<br>Silberbad, wenn dein Schmuck an-<br>gelaufen ist</div></div></div>
    </div>
    <div class="notice" style="top:325px">Perlen müssen vor der Reinigung abgenommen werden. Kristalle werden nicht geschädigt</div>
    <div class="abs warnings">
      <p><b>Wichtig:</b> Da die Schmuckstücke verschluckbare Kleinteile enthalten, bewahre sie bitte außerhalb der Reichweite von Kindern unter drei Jahren auf. Kristall und Glas sind zerbrechlich und müssen vor Stoß und Schlag geschützt werden.</p>
      <p><b>Bitte beachte:</b> Die Kristalle können aufgrund ihres Alters einzelne Gebrauchsspuren aufweisen. Diese sind Teil ihrer Vergangenheit und machen sie nicht weniger schön, sondern verleihen ihnen im Gegenteil eine authentische, lebendige Einzigartigkeit.</p>
    </div>
    <div class="photo" role="img" aria-label="Silberne Ohrringe mit Perlen" style="left:16px;top:425px;width:62px;height:62px;background:linear-gradient(180deg,#f2f2f2,#d6d2cc 60%,#efe6dc)"></div>
    <div class="photo" role="img" aria-label="Schmuckverpackungen und Präsentationsständer mit Kristallanhängern" style="left:96px;top:428px;width:167px;height:60px;background:linear-gradient(180deg,#ffffff,#eeeeef 50%,#e5dfe6)"></div>
    <div class="photo" role="img" aria-label="Silberne Ohrringe mit roten Kristalltropfen" style="left:281px;top:425px;width:52px;height:62px;background:linear-gradient(180deg,#f0f0f0,#d4d2d4 55%,#a0202e)"></div>
  </div>
</section>

</body>
</html>
```